Stationary for a Consulting Firm
The Summit Compass Incorporated
Project: Stationary for a Consulting Firm
Stationary for a Consulting Firm - Consulting
Creative Brief
Professional
Dr. Gordon T. Feld
President
47 Maple Crest Okotoks, AB T2Q 4M9
gfeld@summitcompass.ca
www.summitcompass.ca
Business Cards, Stationary, Fax Cover Sheet, and Envelopes are required
Canada's Summit Compass

```html
<!DOCTYPE html>
<html lang="en">
<head>
<meta charset="utf-8">
<title>The Summit Compass Incorporated — Stationery</title>
<link rel="stylesheet" href="https://fonts.googleapis.com/css2?family=Montserrat:wght@400;600;700&family=Open+Sans:wght@400;600&display=swap">
<style>
  :root{
    --stage:#2c2d4e;
    --paper:#ffffff;
    --brand:#2f9bd8;
    --brand-deep:#1c74b6;
    --ink:#3b4a5a;
    --muted:#8a98a8;
    --rule:#c9d3dd;
    --ghost:#eef5fb;
  }
  *{box-sizing:border-box;margin:0;padding:0}
  html,body{width:1200px;height:864px;overflow:hidden;background:var(--stage)}
  body{position:relative;font-family:"Open Sans",Arial,sans-serif;color:var(--ink)}

  .sheet{position:absolute;background:var(--paper);overflow:hidden;border-radius:2px}
  .ghost-mark{position:absolute;border-radius:50%;background:var(--ghost)}

  .brand{display:flex;align-items:center;gap:6px}
  .brand-dot{border-radius:50%;background:var(--brand);flex:none}
  .brand-name{font-family:"Montserrat",Arial,sans-serif;font-weight:700;color:var(--brand);text-transform:uppercase;line-height:1.05;letter-spacing:.5px}
  .brand--stacked{flex-direction:column;gap:4px;text-align:center}

  /* footer shared by letterhead and fax */
  .sheet-footer{position:absolute;left:18px;right:18px;bottom:14px;display:flex;justify-content:space-between;font-size:5.5px;color:var(--muted);border-top:.6px solid var(--rule);padding-top:5px}
  .sheet-footer span{display:flex;align-items:center;gap:3px}
  .ico{width:6px;height:6px;border-radius:50%;background:var(--brand);flex:none}

  /* letterhead */
  .letterhead{left:40px;top:60px;width:340px;height:440px}
  .letterhead .brand{position:absolute;top:24px;left:0;right:0}
  .letterhead .brand-dot{width:20px;height:20px}
  .letterhead .brand-name{font-size:11px}
  .letterhead .ghost-mark{width:230px;height:230px;left:60px;top:150px}

  /* fax */
  .fax{left:410px;top:60px;width:340px;height:440px}
  .fax .brand{position:absolute;top:24px;left:0;right:0}
  .fax .brand-dot{width:20px;height:20px}
  .fax .brand-name{font-size:11px}
  .fax .ghost-mark{width:230px;height:230px;left:60px;top:170px}
  .fax-title{position:absolute;right:22px;top:88px;font-family:"Montserrat",Arial,sans-serif;font-weight:700;font-size:13px;letter-spacing:1px;color:var(--ink)}
  .fax-table{position:absolute;left:22px;right:22px;top:106px;border-collapse:collapse;width:296px;font-size:6px;color:var(--ink)}
  .fax-table td{border:.7px solid var(--ink);height:15px;padding:0 4px}
  .fax-table .label{width:44px;font-weight:600}
  .fax-checks{position:absolute;left:22px;right:22px;top:176px;display:flex;justify-content:space-between;font-size:5.5px}
  .fax-checks span{display:flex;align-items:center;gap:3px}
  .box{width:6px;height:6px;border:.7px solid var(--ink);border-radius:50%}

  /* envelopes */
  .envelope{left:780px;width:380px;height:165px}
  .envelope-front{top:60px}
  .envelope-front-b{top:520px}
  .envelope-back{top:290px}
  .envelope .ghost-mark{width:170px;height:170px;right:-20px;top:20px}
  .return-block{position:absolute;left:16px;top:16px}
  .return-block .brand-dot{width:14px;height:14px}
  .return-block .brand-name{font-size:8px}
  .return-address{margin-top:5px;font-size:5.5px;color:var(--muted);line-height:1.5}
  .flap{position:absolute;inset:0}
  .envelope-back .brand{position:absolute;left:0;right:0;top:40px}
  .envelope-back .brand-dot{width:16px;height:16px}
  .envelope-back .brand-name{font-size:8px}

  /* business cards */
  .card{top:560px;width:340px;height:194px;border-radius:10px}
  .card-front{left:40px}
  .card-back{left:410px;background:linear-gradient(135deg,var(--brand) 0%,var(--brand-deep) 100%)}
  .card-front .brand{position:absolute;left:28px;top:72px;flex-direction:column;align-items:center;gap:5px;text-align:center}
  .card-front .brand-dot{width:28px;height:28px}
  .card-front .brand-name{font-size:11px}
  .card-divider{position:absolute;left:146px;top:30px;bottom:30px;width:1px;background:var(--brand)}
  .card-person{position:absolute;left:162px;top:32px}
  .card-name{font-family:"Montserrat",Arial,sans-serif;font-weight:600;font-size:12px;color:var(--brand)}
  .card-role{font-size:8px;color:var(--muted);margin-top:2px}
  .card-contacts{position:absolute;left:162px;top:92px;font-size:7.5px;line-height:1.9;color:var(--ink)}
  .card-contacts span{display:flex;align-items:center;gap:5px}
  .card-contacts .ico{width:8px;height:8px}
  .card-front .ghost-mark{width:150px;height:150px;right:-40px;bottom:-60px}
  .card-back .ghost-mark{width:200px;height:200px;left:70px;top:-3px;background:rgba(255,255,255,.12)}
</style>
</head>
<body>

<!-- Letterhead -->
<section class="sheet letterhead" aria-label="Letterhead">
  <div class="ghost-mark"></div>
  <div class="brand brand--stacked">
    <span class="brand-dot"></span>
    <span class="brand-name">Summit<br>Compass</span>
  </div>
  <footer class="sheet-footer">
    <span><i class="ico"></i>47 Maple Crest Okotoks, AB T2Q 4M9</span>
    <span><i class="ico"></i>403.555.0148</span>
    <span><i class="ico"></i>gfeld@summitcompass.ca</span>
    <span><i class="ico"></i>www.summitcompass.ca</span>
  </footer>
</section>

<!-- Fax cover sheet -->
<section class="sheet fax" aria-label="Fax cover sheet">
  <div class="ghost-mark"></div>
  <div class="brand brand--stacked">
    <span class="brand-dot"></span>
    <span class="brand-name">Summit<br>Compass</span>
  </div>
  <div class="fax-title">FAX</div>
  <table class="fax-table">
    <tr><td class="label">To</td><td></td><td class="label">From</td><td></td></tr>
    <tr><td class="label">Company</td><td></td><td class="label">Pages</td><td></td></tr>
    <tr><td class="label">Fax</td><td></td><td class="label">Date</td><td></td></tr>
    <tr><td class="label">Phone</td><td></td><td class="label">Re</td><td></td></tr>
  </table>
  <div class="fax-checks">
    <span><i class="box"></i>Urgent</span>
    <span><i class="box"></i>For Review</span>
    <span><i class="box"></i>Please Comment</span>
    <span><i class="box"></i>Please Reply</span>
  </div>
  <footer class="sheet-footer">
    <span><i class="ico"></i>47 Maple Crest Okotoks, AB T2Q 4M9</span>
    <span><i class="ico"></i>403.555.0148</span>
    <span><i class="ico"></i>gfeld@summitcompass.ca</span>
    <span><i class="ico"></i>www.summitcompass.ca</span>
  </footer>
</section>

<!-- Envelope front -->
<section class="sheet envelope envelope-front" aria-label="Envelope front">
  <div class="ghost-mark"></div>
  <div class="return-block">
    <div class="brand"><span class="brand-dot"></span><span class="brand-name">Summit<br>Compass</span></div>
    <p class="return-address">The Summit Compass Incorporated<br>47 Maple Crest Okotoks, AB T2Q 4M9</p>
  </div>
</section>

<!-- Envelope back -->
<section class="sheet envelope envelope-back" aria-label="Envelope back">
  <svg class="flap" viewBox="0 0 380 165" preserveAspectRatio="none">
    <polyline points="0,0 190,95 380,0" fill="none" stroke="#c9d3dd" stroke-width="1"/>
  </svg>
  <div class="brand brand--stacked">
    <span class="brand-dot"></span>
    <span class="brand-name">Summit<br>Compass</span>
  </div>
</section>

<!-- Envelope front, second -->
<section class="sheet envelope envelope-front-b" aria-label="Envelope front">
  <div class="ghost-mark"></div>
  <div class="return-block">
    <div class="brand"><span class="brand-dot"></span><span class="brand-name">Summit<br>Compass</span></div>
    <p class="return-address">Canada's Summit Compass<br>www.summitcompass.ca</p>
  </div>
</section>

<!-- Business card front -->
<section class="sheet card card-front" aria-label="Business card front">
  <div class="ghost-mark"></div>
  <div class="brand">
    <span class="brand-dot"></span>
    <span class="brand-name">Summit<br>Compass</span>
  </div>
  <div class="card-divider"></div>
  <div class="card-person">
    <div class="card-name">Dr. Gordon T. Feld</div>
    <div class="card-role">President</div>
  </div>
  <div class="card-contacts">
    <span><i class="ico"></i>403.555.0148</span>
    <span><i class="ico"></i>gfeld@summitcompass.ca</span>
    <span><i class="ico"></i>www.summitcompass.ca</span>
    <span><i class="ico"></i>47 Maple Crest Okotoks, AB T2Q 4M9</span>
  </div>
</section>

<!-- Business card back -->
<section class="sheet card card-back" aria-label="Business card back">
  <div class="ghost-mark"></div>
</section>

</body>
</html>
```